Claimwise Helpdesk USA - Email Marketing Creative

Looking for design of email creative for Claimwise Helpdesk USA website. Call to action based email focused on conveying brand, messaging of "Disabled? Unable to Work? You May Qualify for Social Security Disability Benefits", call to action of 'Free Evaluation' or 'Fast, Free, No Obligation Evaluation'. Can use any messaging from the current mock of https://qlnk.example/7XrTm4K . Please focus on imaging of 50+ people if used, red white and blue coloring (patriotic) yet USA looking. Creative must be done in HTML as well as text for easy use and include Email Opt Out link etc. Examples of competitors emails attached. PLEASE DO NOT COPY them. Just use as examples.

Target Market(s)

Disabled American. Age 50+ Looking for help applying, re-applying or handling a social security disability hearing.

Industry/Entity Type

Legal

Font styles to use
Serif
Sans Serif

Colors

Designer to choose colors to be used in the design.

Requirements
Must have
• call to action based html
Nice to have
• strong call to action.
Should not have
• Should not be cookie cutter. Stick to simple yet official looking.

```html
<!DOCTYPE html>
<html lang="en">
<head>
<meta charset="utf-8">
<title>Claimwise Helpdesk USA – Free Evaluation</title>
<link href="https://fonts.googleapis.com/css2?family=Roboto:wght@400;500;700&family=Roboto+Condensed:wght@500;700&display=swap" rel="stylesheet">
<style>
  :root {
    --navy: #0f1838;
    --red: #e4102b;
    --ink: #1b1b1f;
    --body: #5b5b60;
    --muted: #6a6a70;
    --hero-bg: #e5e5e8;
    --panel: #f7f7f8;
    --rule: #dedee2;
    --white: #ffffff;
  }
  * { box-sizing: border-box; margin: 0; padding: 0; }
  html, body { width: 1200px; height: 2980px; overflow: hidden; background: var(--white); }
  body { font-family: "Roboto", Arial, sans-serif; color: var(--ink); position: relative; }

  .top-rule { position: absolute; left: 0; top: 0; width: 1200px; height: 7px; background: var(--red); }

  .brand { position: absolute; left: 92px; top: 40px; display: flex; align-items: center; gap: 18px; }
  .brand-dot { width: 130px; height: 130px; border-radius: 50%; background: var(--navy); }
  .brand-name { width: 240px; font-family: "Roboto Condensed", Arial, sans-serif; font-weight: 700; font-size: 36px; line-height: 1.1; color: var(--navy); }

  .btn-header { position: absolute; left: 727px; top: 66px; width: 381px; height: 78px; border-radius: 39px; background: var(--navy); color: var(--white); font-family: "Roboto", Arial, sans-serif; font-weight: 500; font-size: 33px; display: flex; align-items: center; justify-content: center; text-decoration: none; }

  .hero { position: absolute; left: 0; top: 200px; width: 1200px; height: 634px; background: var(--hero-bg); overflow: hidden; }
  .hero-photo { position: absolute; left: 430px; top: 0; width: 770px; height: 634px;
    background: linear-gradient(90deg, rgba(229,229,232,1) 0%, rgba(222,214,206,0.85) 18%, #cdb9a8 40%, #8e7e74 62%, #5d6f91 80%, #c8c2bb 100%); }
  .hero-copy { position: absolute; left: 90px; top: 120px; }
  .hero-title { font-family: "Roboto Condensed", Arial, sans-serif; font-weight: 700; font-size: 62px; line-height: 82px; color: var(--navy); }
  .hero-title .accent { color: var(--red); display: block; }
  .hero-sub { margin-top: 26px; font-size: 37px; line-height: 50px; color: var(--ink); width: 520px; }
  .hero-banner { position: absolute; left: 92px; top: 439px; width: 923px; height: 59px; background: var(--red); color: var(--white); font-family: "Roboto Condensed", Arial, sans-serif; font-weight: 700; font-size: 30px; display: flex; align-items: center; padding-left: 44px; clip-path: polygon(22px 0, 100% 0, 100% 100%, 0 100%); }

  .seal { position: absolute; width: 118px; height: 118px; border-radius: 50%; background: var(--white); display: flex; align-items: center; justify-content: center; }
  .seal span { width: 70px; height: 70px; border-radius: 50%; background: var(--navy); }
  .seal-top { left: 541px; top: 775px; }
  .seal-bottom { left: 541px; top: 2769px; z-index: 2; }

  .intro { position: absolute; left: 120px; top: 916px; width: 960px; text-align: center; font-size: 28px; line-height: 59px; color: var(--body); }

  .features { position: absolute; left: 94px; top: 1141px; width: 1014px; height: 269px; background: var(--panel); border: 2px solid var(--rule); padding: 20px 0 0 30px; display: flex; }
  .features ul { list-style: none; }
  .features ul:first-child { width: 536px; }
  .features li { position: relative; padding-left: 62px; font-weight: 500; font-size: 30px; line-height: 55px; color: var(--ink); }
  .features li svg { position: absolute; left: 0; top: 15px; width: 28px; height: 28px; }

  .body-copy { position: absolute; left: 113px; width: 974px; font-size: 28px; line-height: 59px; color: var(--body); text-align: justify; text-align-last: center; }
  .copy-a { top: 1467px; }
  .copy-b { top: 1775px; }

  .btn-cta { position: absolute; left: 382px; top: 2199px; width: 436px; height: 77px; border-radius: 39px; background: var(--red); color: var(--white); font-weight: 500; font-size: 33px; display: flex; align-items: center; padding-left: 56px; text-decoration: none; }
  .btn-cta svg { position: absolute; right: 14px; top: 16px; width: 46px; height: 46px; }

  .divider { position: absolute; left: 90px; top: 2366px; width: 1018px; height: 2px; background: var(--rule); }

  .optout { position: absolute; left: 60px; top: 2425px; width: 1080px; text-align: center; font-weight: 500; font-size: 33px; line-height: 54px; color: var(--ink); }
  .optout a { color: var(--red); text-decoration: underline; }

  .contact { position: absolute; left: 0; top: 2560px; width: 1200px; text-align: center; font-size: 28px; line-height: 40px; color: var(--muted); }
  .contact svg { width: 22px; height: 26px; vertical-align: -4px; margin-right: 8px; }
  .contact .sep { margin: 0 16px; }

  .social { position: absolute; left: 411px; top: 2660px; display: flex; gap: 15px; }
  .social span { width: 64px; height: 64px; border-radius: 50%; display: block; }
  .social .s1 { background: #1a2452; }
  .social .s2 { background: #1f97e0; }
  .social .s3 { background: #e4102b; }
  .social .s4 { background: #a3814a; }
  .social .s5 { background: #1878b8; }

  .footer { position: absolute; left: 0; top: 2854px; width: 1200px; height: 126px; background: var(--navy); color: var(--white); font-size: 24px; display: flex; align-items: center; justify-content: center; padding-top: 22px; }
</style>
</head>
<body>
  <div class="top-rule"></div>

  <header>
    <div class="brand">
      <span class="brand-dot"></span>
      <span class="brand-name">Claimwise Helpdesk USA</span>
    </div>
    <a class="btn-header" href="https://qlnk.example/7XrTm4K">FREE EVALUATION</a>
  </header>

  <section class="hero">
    <div class="hero-photo" role="img" aria-label="Smiling older couple at home sharing a laptop while one talks on the phone"></div>
    <div class="hero-copy">
      <h1 class="hero-title">UNABLE TO WORK<span class="accent">DUE TO DISABILITY?</span></h1>
      <p class="hero-sub">We help Americans get the benefits they deserve!</p>
    </div>
    <div class="hero-banner">YOU MAY QUALITY FOR BENEFITS OF UP TO $2,642.00/MONTH!</div>
  </section>
  <div class="seal seal-top"><span></span></div>

  <p class="intro">Sed ut perspiciatis unde omnis iste natus error sit voluptatem accusantium doloremque laudantium, totam rem aperiam, eaque ipsa quae ab illo inventore veritatis et quasi architecto beatae vitae dicta sunt explicabo.</p>

  <section class="features">
    <ul>
      <li><svg viewBox="0 0 28 28"><circle cx="14" cy="14" r="14" fill="#e4102b"/><path d="M8 14.5l4 4 8-8" stroke="#fff" stroke-width="3.2" fill="none" stroke-linecap="round" stroke-linejoin="round"/></svg>We deal with the government</li>
      <li><svg viewBox="0 0 28 28"><circle cx="14" cy="14" r="14" fill="#e4102b"/><path d="M8 14.5l4 4 8-8" stroke="#fff" stroke-width="3.2" fill="none" stroke-linecap="round" stroke-linejoin="round"/></svg>100% Free Evaluation Service!</li>
      <li><svg viewBox="0 0 28 28"><circle cx="14" cy="14" r="14" fill="#e4102b"/><path d="M8 14.5l4 4 8-8" stroke="#fff" stroke-width="3.2" fill="none" stroke-linecap="round" stroke-linejoin="round"/></svg>Get the benefits you deserve!</li>
    </ul>
    <ul>
      <li><svg viewBox="0 0 28 28"><circle cx="14" cy="14" r="14" fill="#e4102b"/><path d="M8 14.5l4 4 8-8" stroke="#fff" stroke-width="3.2" fill="none" stroke-linecap="round" stroke-linejoin="round"/></svg>Fast,Easy and secure!</li>
      <li><svg viewBox="0 0 28 28"><circle cx="14" cy="14" r="14" fill="#e4102b"/><path d="M8 14.5l4 4 8-8" stroke="#fff" stroke-width="3.2" fill="none" stroke-linecap="round" stroke-linejoin="round"/></svg>Takes less tha 2 minutes!</li>
      <li><svg viewBox="0 0 28 28"><circle cx="14" cy="14" r="14" fill="#e4102b"/><path d="M8 14.5l4 4 8-8" stroke="#fff" stroke-width="3.2" fill="none" stroke-linecap="round" stroke-linejoin="round"/></svg>Previous denials &amp; new applicants!</li>
    </ul>
  </section>

  <p class="body-copy copy-a">Nemo enim ipsam voluptatem quia voluptas sit aspernatur aut odit aut fugit, sed quia consequuntur magni dolores eos qui ratione voluptatem sequi nesciunt. Neque porro quisquam est, qui dolorem ipsum quia dolor sit amet, consectetur, adipisci velit, sed quia non numquam eius modi tempora incidunt ut labore et dolore magnam aliquam quaerat voluptatem.</p>

  <p class="body-copy copy-b">But I must explain to you how all this mistaken idea of denouncing pleasure and praising pain was born and I will give you a complete account of the system, and expound the actual teachings of the great explorer of the truth, the master-builder of humBut I must explain to you how all this mistaken idea of denouncing pleasure and praising pain was born and I will give you a complete account of the system, and expound the actual teachings</p>

  <a class="btn-cta" href="https://qlnk.example/7XrTm4K">FREE EVALUATION
    <svg viewBox="0 0 46 46"><circle cx="23" cy="23" r="21" fill="#fff"/><circle cx="23" cy="23" r="13" fill="none" stroke="#e4102b" stroke-width="3"/><path d="M17 23h11M23.5 18l5 5-5 5" stroke="#e4102b" stroke-width="3" fill="none" stroke-linecap="round" stroke-linejoin="round"/></svg>
  </a>

  <div class="divider"></div>

  <footer>
    <p class="optout">You need tis newsletter because you have subscribed to exclusive onlinepromo Newsletter to subscribe,please <a href="https://qlnk.example/7XrTm4K">Visit here</a></p>
    <p class="contact">
      <svg viewBox="0 0 22 26"><path d="M11 1C5.8 1 2 4.9 2 9.8 2 16 11 25 11 25s9-9 9-15.2C20 4.9 16.2 1 11 1z" fill="#e4102b"/><circle cx="11" cy="9.8" r="3.4" fill="#fff"/></svg>234,Excepteur sint ocat cupi<span class="sep">|</span><svg viewBox="0 0 24 24"><path d="M6.6 10.8a15.1 15.1 0 006.6 6.6l2.2-2.2c.3-.3.7-.4 1-.2 1.1.4 2.3.6 3.6.6.6 0 1 .4 1 1V20c0 .6-.4 1-1 1C10.6 21 3 13.4 3 4c0-.6.4-1 1-1h3.5c.6 0 1 .4 1 1 0 1.3.2 2.5.6 3.6.1.3 0 .7-.2 1z" fill="#e4102b"/></svg>1 800 555 0142
    </p>
    <div class="social" aria-label="Social media links">
      <span class="s1"></span><span class="s2"></span><span class="s3"></span><span class="s4"></span><span class="s5"></span>
    </div>
    <div class="seal seal-bottom"><span></span></div>
    <div class="footer">Copyrights © 2019, Claimwise Helpdesk USA . All Rights Reserved.</div>
  </footer>
</body>
</html>
```